Exciting business card design for diesel performance and offroad business!!

We need a business card design that looks good and stands out. I don't want a plain old boring business card that you forget about and throw away at the end of the day. We are a diesel performance and truck accessory business that sell and install the industries biggest brands and best parts out there!

Industry/Entity Type

Business

Contact Information for Business Card

Davin Throope (Owner) 260-555-0173
steadfast.garage@mailvoro.com
Truck and Off-Road Performance and Accessories

Requirements
Must have
• A great look and feel about it. My logo needs to be in center of the card just like the attached picture. On the back I want it to have a list of items we offer
• Truck and Vorn: Lift and Leveling Kits, Intake and Exhaust Systems, Custom Tuning, Wheels and Tires, Steps, Bed Covers, Floor Liners, Custom Lighting, Turbos and Piping, Gauges, Much More!
• UTV: Suspension, Roll Cage, Doors, Exhaust, Tuning, Turbo Kits, Stereo, Wheels/Tires, Custom Lighting, Clutching, Much More!!

```html
<!DOCTYPE html>
<html lang="en">
<head>
<meta charset="utf-8">
<title>Steadfast Garage — Business Card</title>
<link rel="stylesheet" href="https://fonts.googleapis.com/css2?family=Open+Sans:wght@400;600;700&display=swap">
<style>
  :root {
    --bg: #e9e6e2;
    --charcoal: #2f3034;
    --charcoal-deep: #26272a;
    --white: #ffffff;
    --red: #d9232a;
    --grey-text: #6b6b6b;
    --light-text: #e4e4e4;
    --brand-grey: #9a9ca0;
  }
  * { box-sizing: border-box; margin: 0; padding: 0; }
  html, body { width: 1200px; height: 1023px; overflow: hidden; }
  body {
    background: var(--bg);
    font-family: "Open Sans", Arial, sans-serif;
    position: relative;
  }
  .card {
    position: absolute;
    left: 220px;
    width: 760px;
    height: 434px;
    border-radius: 22px;
    overflow: hidden;
    box-shadow: 0 8px 24px rgba(0,0,0,0.18);
  }
  /* Front */
  .card-front { top: 48px; background: var(--white); }
  .front-art { position: absolute; inset: 0; }
  .brand-mark {
    position: absolute; right: 48px; top: 40px;
    display: flex; align-items: center; gap: 12px;
  }
  .brand-dot { width: 18px; height: 18px; border-radius: 50%; background: var(--brand-grey); }
  .brand-name {
    font-weight: 700; font-size: 22px; letter-spacing: 3px;
    color: var(--brand-grey); text-transform: uppercase;
  }
  .owner { position: absolute; left: 48px; top: 62px; }
  .owner-name { color: var(--red); font-weight: 700; font-size: 26px; }
  .owner-role { color: var(--grey-text); font-size: 15px; font-weight: 400; }
  .contact { position: absolute; left: 48px; top: 124px; list-style: none; }
  .contact li {
    display: flex; align-items: center; gap: 12px;
    color: var(--grey-text); font-size: 16px; margin-bottom: 12px;
  }
  .contact svg { width: 20px; height: 20px; flex: none; }
  .tagline {
    position: absolute; right: 40px; top: 206px;
    background: var(--red); color: var(--white);
    font-weight: 700; font-size: 19px;
    padding: 8px 18px; border-radius: 6px;
  }
  .services { position: absolute; left: 48px; top: 268px; right: 40px; list-style: none; }
  .service { display: flex; gap: 14px; margin-bottom: 22px; }
  .service-title {
    flex: none; width: 150px; color: var(--red);
    font-size: 17px; font-weight: 600; display: flex; gap: 8px;
  }
  .service-title::before { content: "\25B6"; font-size: 12px; line-height: 24px; }
  .service-items { color: var(--light-text); font-size: 13.5px; line-height: 1.5; }
  /* Back */
  .card-back { top: 542px; background: var(--charcoal); }
  .back-art { position: absolute; inset: 0; }
  .back-brand {
    position: absolute; inset: 0;
    display: flex; align-items: center; justify-content: center; gap: 16px;
  }
  .back-brand .brand-dot { width: 26px; height: 26px; background: #c7c8cb; }
  .back-brand .brand-name { font-size: 38px; letter-spacing: 6px; color: #c7c8cb; }
</style>
</head>
<body>
  <section class="card card-front" aria-label="Business card front">
    <svg class="front-art" viewBox="0 0 760 434" aria-hidden="true">
      <polygon points="0,244 760,214 760,434 0,434" fill="var(--charcoal)"/>
      <polygon points="0,240 760,210 760,214 0,244" fill="var(--red)"/>
    </svg>
    <div class="brand-mark">
      <span class="brand-dot"></span>
      <span class="brand-name">Steadfast Garage</span>
    </div>
    <div class="owner">
      <span class="owner-name">Davin Throope,</span>
      <span class="owner-role">Owner</span>
    </div>
    <ul class="contact">
      <li>
        <svg viewBox="0 0 20 20"><circle cx="10" cy="10" r="8.5" fill="none" stroke="var(--red)" stroke-width="1.6"/><path d="M7 6.2l1.6-.4 1 2.2-1 .8a5 5 0 0 0 2.6 2.6l.8-1 2.2 1-.4 1.6c-3.6.4-7.2-3.2-6.8-6.8z" fill="var(--red)"/></svg>
        260-555-0173
      </li>
      <li>
        <svg viewBox="0 0 20 20"><rect x="2" y="4.5" width="16" height="11" fill="none" stroke="var(--red)" stroke-width="1.6"/><path d="M2 4.5l8 6.5 8-6.5M2 15.5l6-5.5M18 15.5l-6-5.5" fill="none" stroke="var(--red)" stroke-width="1.4"/></svg>
        steadfast.garage@mailvoro.com
      </li>
    </ul>
    <div class="tagline">Truck and Off-Road Performance and Accessories</div>
    <ul class="services">
      <li class="service">
        <span class="service-title">Truck and Vorn</span>
        <span class="service-items">Lift and Leveling Kits, Intake and Exhaust Systems, Custom Tuning, Wheels and Tires, Steps, Bed Covers, Floor Liners, Custom Lighting, Turbos and Piping, Gauges, Much More!</span>
      </li>
      <li class="service">
        <span class="service-title">UTV</span>
        <span class="service-items">Suspension, Roll Cage, Doors, Exhaust, Tuning, Turbo Kits, Stereo, Wheels/Tires, Custom Lighting, Clutching, Much More!!</span>
      </li>
    </ul>
  </section>

  <section class="card card-back" aria-label="Business card back">
    <svg class="back-art" viewBox="0 0 760 434" aria-hidden="true">
      <polygon points="0,0 230,0 215,14 0,14" fill="var(--red)"/>
      <polygon points="0,420 760,420 760,434 0,434" fill="var(--red)"/>
    </svg>
    <div class="back-brand">
      <span class="brand-dot"></span>
      <span class="brand-name">Steadfast Garage</span>
    </div>
  </section>
</body>
</html>
```